PageForge Design Project for lornabethwickes.com.au

Update
PLEASE NOTE ...Coding Required

I need a simple website to display my art. There will be 4 different categories - FloraGrandis (botanical art), Oceanlife, Travel Sketchbook, Portraits. There needs to be room for an introduction to me and my work,photos of my studio and views from here and a description of each individual piece. I will probably display no more than 10 pieces in category. Obviously I need to change photos on a regular basis.

I would also like to include a CoinPort button to be connected to my CoinPort account.

I have already started to do a website on PageForge but am finding it too hard to do.

Thank you

Lorna
Updates

Reason: I have provided a deadline extension as I feel the initial lead up time could be too short. Hope that helps you. Lorna

Dear designers. Thankyou all so much for submitting some beautiful designs. I will spend time this weekend evaluating them but as the closing date is January 19, I will not make final decisions until then.  You have probably received an update by now butI  just want to mention that Coding is required.

Cheers

Lorna

Thank you Designers for your patience.  I have been advised by ArtistHive that I cannot make a decision until the deadline has passed, so will let you know on Saturday.

Thank you.
Lorna.

Target Market(s)

35 to 75 who want to buy art and very personal gifts

Industry/Entity Type

Travel

Requirements
Must have
• Ability to change photos often. Modern, elegant, streamlined
Nice to have
• The colour green, an elegant font - sans serif and definitely not courier; room for a photo of me (maybe), and an interesting headline font
Should not have
• quirky, cartooney, retro.

```html
<!DOCTYPE html>
<html lang="en">
<head>
<meta charset="utf-8">
<title>Lorna Beth Wickes – Art Store</title>
<link rel="stylesheet" href="https://fonts.googleapis.com/css2?family=Asap+Condensed:wght@400;500&family=Gelasio:wght@400;500&family=Rokkitt:wght@500;600;700&display=swap">
<style>
:root{
  --green-dark:#647d2e;
  --green-text:#5f7a28;
  --green-soft:#c8de9c;
  --green-pale:#bcd58a;
  --green-light:#d4e6ae;
  --ink:#222;
  --body:#333;
  --grey-band:#f2f2f2;
  --rule:#d4d4d4;
  --white:#fff;
}
*{margin:0;padding:0;box-sizing:border-box}
html,body{width:1200px;height:1019px;overflow:hidden}
body{background:var(--green-soft);font-family:"Gelasio",Georgia,serif;color:var(--body);position:relative}
a{color:inherit;text-decoration:none}
.abs{position:absolute}

.topbar{left:0;top:0;width:1200px;height:73px;background:var(--green-dark)}
.brand{left:179px;top:21px;font-family:"Asap Condensed",sans-serif;font-size:26px;color:var(--white);letter-spacing:.3px}
.cart{left:783px;top:24px;display:flex;align-items:center;gap:9px;font-size:11px;color:var(--green-light)}
.cart-bag{width:19px;height:27px}

.util-nav{left:180px;top:90px;font-size:11px;color:var(--green-text)}
.util-nav span{color:#777;margin:0 4px}
.currency-label{left:691px;top:90px;font-size:11px;color:#666}
.select{left:743px;top:88px;width:88px;height:21px;background:var(--white);border:1px solid #bbb;font-size:11px;padding:3px 6px;color:#222}
.select::after{content:"";position:absolute;right:6px;top:8px;border:4px solid transparent;border-top-color:#666}
.search{left:840px;top:88px;width:173px;height:21px;background:var(--white);border:1px solid #bbb;font-size:11px;padding:3px 6px;color:#222}
.search svg{position:absolute;right:8px;top:6px}

.strip-white{left:177px;top:127px;width:845px;height:4px;background:var(--white)}
.strip-green{left:177px;top:131px;width:845px;height:13px;background:var(--green-dark)}
.main-nav{left:177px;top:148px;width:845px;height:44px;background:var(--white);display:flex;align-items:center;justify-content:space-between;padding:0 34px;border-bottom:2px solid #e4e4e4}
.main-nav a{font-family:"Rokkitt",serif;font-weight:600;font-size:16px;color:var(--green-text)}
.main-nav i{width:1px;height:24px;border-left:2px solid var(--green-pale);transform:skewX(-20deg)}

.hero{left:177px;top:193px;width:845px;height:279px;background:linear-gradient(#ececec,#e2e2e2)}
.hero-art{left:596px;top:0;width:249px;height:279px;background:radial-gradient(ellipse at 45% 35%,#ee6a4c 0%,#f39a7c 28%,rgba(236,226,224,.6) 60%,rgba(228,228,228,0) 80%)}
.avatar{left:57px;top:61px;width:117px;height:117px;background:var(--white);border:2px solid #d8d8d8}
.avatar-fill{position:absolute;inset:6px;background:linear-gradient(#f4f4f4,#dcdcdc)}
.hero-title{left:184px;top:63px;font-family:"Rokkitt",serif;font-weight:600;font-size:16px;color:var(--ink)}
.hero-text{left:184px;top:95px;width:384px;font-size:10px;letter-spacing:-.15px;line-height:20.3px;color:#333}
.hero-more{left:184px;top:197px;font-size:10.5px;color:var(--green-text)}
.dots{left:184px;top:238px;display:flex;gap:1px}
.dots b{width:13px;height:13px;border-radius:50%;background:var(--green-pale)}
.dots b:first-child{background:var(--green-dark)}

.featured{left:177px;top:472px;width:845px;height:278px;background:var(--white)}
.sec-title{font-family:"Rokkitt",serif;font-weight:700;font-size:15.5px;color:var(--ink);letter-spacing:.1px}
.sec-rule{height:2px;background:var(--rule)}
.tabs{left:53px;top:68px;display:flex;gap:30px;font-family:"Rokkitt",serif;font-weight:500;font-size:14.5px;color:#111}
.tabs .active{color:var(--green-text);position:relative}
.tabs .active::after{content:"";position:absolute;left:50%;bottom:-9px;margin-left:-10px;border:5px solid transparent;border-left-width:10px;border-right-width:10px;border-top-color:var(--green-dark)}
.arrows{left:771px;top:67px;display:flex;gap:2px}
.arrows svg{width:19px;height:19px}
.thumb{top:105px;width:169px;height:156px;border:1px solid #ccc}
.t1{left:38px;background:radial-gradient(circle at 45% 45%,#f0735a,#f7b6a4 45%,#f3efee 75%)}
.t2{left:239px;background:linear-gradient(135deg,#e8ecdf,#c7d4b4 50%,#e6e9df)}
.t3{left:439px;background:radial-gradient(circle at 35% 45%,#3f7a32,#6c9a52 45%,#f2efee 80%)}
.t4{left:640px;background:linear-gradient(#e050b5 0%,#3fb9c4 40%,#e9e64a 70%,#3fb2c0)}

.blog{left:177px;top:750px;width:845px;height:189px;background:var(--grey-band)}
.post{top:56px;width:216px;font-size:10.5px}
.post h3{font-weight:400;font-size:10.5px;color:var(--green-text)}
.post time{display:block;margin-top:14px;color:#7a9a4a}
.post p{margin-top:14px;color:#222;font-size:10px;line-height:15.5px}
.post a{display:block;margin-top:10px;color:var(--green-text)}

.footer{left:177px;top:939px;width:845px;height:80px;background:var(--white)}
.foot-links{left:21px;top:20px;font-size:10.5px;color:#333}
.copy{left:21px;top:48px;font-size:10.5px;color:#333}
.pay{right:20px;top:18px;display:flex;gap:3px}
.pay span{height:16px;padding:0 4px;border:1px solid #bbb;background:#f4f4f4;font-size:7px;line-height:14px;color:#445}
.social{right:22px;top:50px;display:flex;gap:8px}
.social span{width:14px;height:14px;background:#8a9ab0}
.social .rss{background:#e6892f}
</style>
</head>
<body>

<header class="abs topbar"></header>
<div class="abs brand">LORNA BETH WICKES</div>
<div class="abs cart">
  <svg class="cart-bag" viewBox="0 0 19 27"><path d="M5 9V5a4.5 4.5 0 0 1 9 0v4" fill="none" stroke="#c7dc98" stroke-width="2"/><rect x="0" y="8" width="19" height="19" rx="2" fill="#c7dc98"/></svg>
  <span>Shopping Cart: Now in your cart (0)&nbsp; items</span>
</div>

<nav class="abs util-nav"><a>Online Store</a><span>/</span><a>About Us</a><span>/</span><a>Delivery</a><span>/</span><a>FAQs</a><span>/</span><a>Contacts</a></nav>
<div class="abs currency-label">Currency:</div>
<div class="abs select">US Dollar</div>
<div class="abs search">Search
  <svg width="7" height="7" viewBox="0 0 7 7"><circle cx="3" cy="3" r="2.2" fill="none" stroke="#888"/><path d="M4.6 4.6 6.5 6.5" stroke="#888"/></svg>
</div>

<div class="abs strip-white"></div>
<div class="abs strip-green"></div>
<nav class="abs main-nav">
  <a>Home</a><i></i><a>New Products</a><i></i><a>Specials</a><i></i><a>All Products</a><i></i><a>Reviews</a><i></i><a>Contacts</a><i></i><a>FAQs</a>
</nav>

<section class="abs hero">
  <div class="abs hero-art" role="img" aria-label="Watercolour of a large red-orange flower on a branch"></div>
  <div class="abs avatar"><div class="avatar-fill" role="img" aria-label="Placeholder portrait of the artist"></div></div>
  <h1 class="abs hero-title">Welcome to Our Lornabeth Wickes</h1>
  <p class="abs hero-text">Duis sapien libero, pulvinar vel porta ac, lacinia sed libero. Aenean ut libero purus, ac congue lorem. Aenean vel urna sapien, congue cursus nunc. Duis sit amet fermentum ante. Cras lobortis malesuada mauris, eget feugiat velit luctus vitae. Sed volutpat tempus elit, nec tempus lorem lacinia vitae. Nulla sed nulla quam.</p>
  <a class="abs hero-more">Read More...</a>
  <div class="abs dots"><b></b><b></b><b></b><b></b></div>
</section>

<section class="abs featured">
  <h2 class="abs sec-title" style="left:20px;top:23px">FEATURED WORK</h2>
  <div class="abs sec-rule" style="left:20px;top:48px;width:807px"></div>
  <div class="abs tabs"><span class="active">FLORAGRANDIS</span><span>OCEANLIFE</span><span>TRAVEL SKETCHBOOK</span><span>PORTRAITS</span></div>
  <div class="abs arrows">
    <svg viewBox="0 0 19 19"><circle cx="9.5" cy="9.5" r="9.5" fill="#666"/><path d="M11 5.5 7 9.5l4 4" fill="none" stroke="#fff" stroke-width="2"/></svg>
    <svg viewBox="0 0 19 19"><circle cx="9.5" cy="9.5" r="9.5" fill="#666"/><path d="M8 5.5l4 4-4 4" fill="none" stroke="#fff" stroke-width="2"/></svg>
  </div>
  <div class="abs thumb t1" role="img" aria-label="Watercolour of a red-orange flower"></div>
  <div class="abs thumb t2" role="img" aria-label="Painting of white daisies among grass"></div>
  <div class="abs thumb t3" role="img" aria-label="Botanical study of green leaves with pink blossoms"></div>
  <div class="abs thumb t4" role="img" aria-label="Vivid painting of a pink and yellow tropical bloom on turquoise"></div>
</section>

<section class="abs blog">
  <h2 class="abs sec-title" style="left:20px;top:16px">BLOG UPDATES</h2>
  <div class="abs sec-rule" style="left:20px;top:40px;width:807px"></div>
  <article class="abs post" style="left:30px">
    <h3>Quisque nisi arcu, mattis nec porttitor eget,</h3>
    <time>Jan 10,2013</time>
    <p>Lorem ipsum dolor sit amet, consectetueradipiscing elit. Donec molestie. Sed aliquamsem ut arcu.</p>
    <a>read more...</a>
  </article>
  <article class="abs post" style="left:314px">
    <h3>Mattis nec porttitor eget,Quisque nisi arcu,</h3>
    <time>Jan 10,2013</time>
    <p>Consectetueradipiscing elit. Donec molestie. Sed aliquamsem ut arcu. Lorem ipsum dolor sit amet,</p>
    <a>read more...</a>
  </article>
  <article class="abs post" style="left:597px;width:213px">
    <h3>Nisi arcu, mattis nec porttitor eget,</h3>
    <time>Jan 10,2013</time>
    <p>Donec molestie. Sed aliquamsem ut arcu. Lorem ipsum dolor sit amet, consectetueradipiscing elit.</p>
    <a>read more...</a>
  </article>
</section>

<footer class="abs footer">
  <div class="abs foot-links">Home / New Products / Specials / All Products / Reviews / Contacts / FAQs</div>
  <div class="abs copy">© Copyright 2013, Lornabeth Wickes, All Rights Reserved</div>
  <div class="abs pay"><span>Kestrel</span><span>Halcyon</span><span>Tarragon</span><span>CoinPort</span></div>
  <div class="abs social">
    <span role="img" aria-label="Friendly"></span>
    <span role="img" aria-label="Chirper"></span>
    <span role="img" aria-label="ProLink"></span>
    <span class="rss" role="img" aria-label="News feed"></span>
    <span role="img" aria-label="Searchly"></span>
  </div>
</footer>

</body>
</html>
```